Wein-Etiketten gesucht
Zielgruppe
Familien geführtes Weingut. eine neue Etikettenlinie soll das bisherige Wein Sortiment ergänzen.
Wein: eine 3er Serie aus rot weiss und rose modern ausgebaut
Plazierung: Online, im Getränke und Weinfachhandel.
Zielgruppe: Moderne Weintrinker
bisherige Weinlinien: www.kellbergwein.de
Aufgabenstellung
Das Etikett soll reduziert sein.
Etikettenformat b127mm h90mm kann ggf angepasst werden.
Weinflasche bordeaux farbe antik
Kapsel schwarz matt kann ggf auch angepasst werden.
die Pflichtangaben sollten am rechten Rand stehen. (das Etikett kann auch breiter als 127 sein, dann verschwinden diese aus dem Sichtbereich.) alternativ ist auch ein Rückenetikett denkbar.
Druck erfolgt im 4c ggf mit Heißfolienprägung Gold

```html
<!DOCTYPE html>
<html lang="de">
<head>
<meta charset="utf-8">
<title>Kellberg Kern Erstling – Etikett</title>
<link href="https://fonts.googleapis.com/css2?family=Montserrat:wght@400;500&family=Barlow+Condensed:wght@400;500&display=swap" rel="stylesheet">
<style>
  :root {
    --paper: #ffffff;
    --ink: #000000;
    --gold: #cbb95c;
    --page: #ffffff;
    --edge: rgba(0,0,0,0.18);
  }
  html, body {
    margin: 0;
    padding: 0;
    width: 720px;
    height: 1200px;
    overflow: hidden;
    background: var(--page);
  }
  .label {
    position: absolute;
    left: 40px;
    top: 394px;
    width: 640px;
    height: 412px;
    background: var(--paper);
    box-shadow: 0 0 3px var(--edge);
    overflow: hidden;
    color: var(--ink);
  }
  .gold-bar {
    position: absolute;
    left: 391px;
    top: 0;
    width: 42px;
    height: 89px;
    background: var(--gold);
  }
  .winery-name {
    position: absolute;
    right: 267px;
    top: 24px;
    margin: 0;
    font-family: "Montserrat", sans-serif;
    font-weight: 500;
    font-size: 24px;
    line-height: 1;
    color: var(--ink);
  }
  .wine-name {
    position: absolute;
    left: 283px;
    top: 128px;
    width: 92px;
    height: 252px;
    margin: 0;
    writing-mode: vertical-rl;
    transform: rotate(180deg);
    font-family: "Montserrat", sans-serif;
    font-weight: 400;
    font-size: 86px;
    line-height: 92px;
    text-align: left;
    letter-spacing: 0;
  }
  .edition-block {
    position: absolute;
    left: 0;
    top: 293px;
    width: 263px;
    height: 119px;
    background: var(--ink);
  }
  .edition-name {
    position: absolute;
    right: 11px;
    top: 12px;
    margin: 0;
    font-family: "Montserrat", sans-serif;
    font-weight: 500;
    font-size: 18px;
    color: var(--paper);
    letter-spacing: 0.2px;
  }
  .mandatory {
    position: absolute;
    left: 522px;
    width: 120px;
    text-align: center;
    font-family: "Barlow Condensed", sans-serif;
    line-height: 19px;
    margin: 0;
  }
  .mandatory--origin {
    top: 85px;
    font-weight: 500;
    font-size: 14px;
  }
  .mandatory--alcohol {
    top: 264px;
    font-weight: 400;
    font-size: 12px;
  }
  .mandatory--apnr {
    top: 285px;
    font-weight: 400;
    font-size: 9.5px;
  }
  .mandatory--bottler {
    top: 323px;
    font-weight: 400;
    font-size: 13px;
  }
</style>
</head>
<body>
  <main class="label" aria-label="Weinetikett Kern Erstling">
    <div class="gold-bar"></div>
    <p class="winery-name">Kellberg</p>

    <h1 class="wine-name">KERN</h1>

    <div class="edition-block">
      <p class="edition-name">ERSTLING</p>
    </div>

    <p class="mandatory mandatory--origin">Württemberg<br>Rotwein<br>2020</p>
    <p class="mandatory mandatory--alcohol">14,5%vol</p>
    <p class="mandatory mandatory--apnr">A.P.Nr: 314 072 21</p>
    <p class="mandatory mandatory--bottler">Gutsabfüllung<br>Weingut<br>J. Kellberg</p>
  </main>
</body>
</html>
```